Postcard Design

We are an exterior house wash company looking to design postcards to promote our business. we clean all types roofs and all types houses and all types of decks and all types of surfaces with a low pressure soft wash system.we also try to educate customers about the options and offer a maintenance program so their property is never dirty again, we use 100% biodegradable solutions to achieve results! our method outperforms traditional washing methods and remains clean 5 times longer,our method is 100% damage free,never pressure wash again!! our method is recommended by all manufactures,the NO pressure method,this method cleans so good you won't believe your eyes! guaranteed call today 207-555-0148 also want to add residential and commercial work and all hoa's(home owners assoc) also group rates available ,please use house washing logo provided,and roof washing logo,also the name of business is Brightfold exterior house washing thanks

Industry/Entity Type

Biodegradable

Requirements
Must have
• company name (Brightfold exterior house washing),logos provided(house wash,roof wash),also pics provided,thank you

```html
<!DOCTYPE html>
<html lang="en">
<head>
<meta charset="utf-8">
<title>Brightfold Exterior House Washing – Postcard</title>
<link href="https://fonts.googleapis.com/css2?family=Archivo+Black&family=Arimo:ital,wght@0,400;0,700;1,700&display=swap" rel="stylesheet">
<style>
  :root {
    --bg: #2a2a2c;
    --card: #0b0b0c;
    --blue: #0d4fb0;
    --green: #1fb40f;
    --yellow: #f5d10a;
    --white: #ffffff;
    --ink: #111111;
    --photo-a: #7c8a6c;
    --photo-b: #c9c7bd;
    --siding-a: #e6e4dc;
    --siding-b: #9a9891;
  }
  * { box-sizing: border-box; margin: 0; padding: 0; }
  html, body { width: 1200px; height: 847px; overflow: hidden; }
  body { background: var(--bg); position: relative; font-family: "Arimo", Arial, sans-serif; }

  .postcard {
    position: absolute; top: 238px; width: 555px; height: 370px;
    background: var(--card); overflow: hidden;
  }
  .postcard--front { left: 30px; }
  .postcard--back { left: 615px; }

  .header-band { position: absolute; left: 0; top: 0; width: 555px; height: 45px; }
  .brand-title {
    position: absolute; left: 12px; top: 9px; width: 535px;
    font-family: "Archivo Black", Arial, sans-serif; font-size: 22px;
    color: var(--yellow); white-space: nowrap; letter-spacing: 0.2px;
  }

  .intro-box {
    position: absolute; left: 8px; top: 55px; width: 215px; height: 258px;
    background: var(--white); color: var(--ink);
    font-weight: 700; font-size: 13.4px; line-height: 1.5; text-align: center;
    padding: 22px 12px 0;
  }

  .photo-row { position: absolute; left: 232px; top: 52px; display: flex; gap: 4px; }
  .photo { width: 103px; height: 80px; background: linear-gradient(160deg, var(--photo-b), var(--photo-a)); }
  .photo:first-child { background: linear-gradient(160deg, #8fa07a, #3f4a3a); }

  .service-badge {
    position: absolute; top: 140px; width: 130px; height: 62px; border-radius: 50%;
    background: radial-gradient(circle at 50% 40%, #3aa7c8, #14506a);
    border: 3px solid #e8eef2;
  }
  .service-badge--roof { left: 237px; }
  .service-badge--house { left: 400px; }

  .quality-seal {
    position: absolute; left: 236px; top: 208px; width: 82px; height: 82px; border-radius: 50%;
    background: radial-gradient(circle, #e0b347, #7a5512);
  }

  .promise-band {
    position: absolute; left: 330px; top: 205px; width: 225px; height: 36px; background: var(--green);
    color: var(--white); font-weight: 700; font-style: italic; padding-left: 22px;
    display: flex; align-items: baseline; gap: 6px;
  }
  .promise-band .lead { font-size: 17px; padding-top: 8px; }
  .promise-band .figure { font-size: 30px; }
  .promise-note {
    position: absolute; left: 348px; top: 244px; width: 188px; height: 38px; background: var(--blue);
    color: var(--white); font-weight: 700; font-size: 12.5px; line-height: 1.25; text-align: center;
    padding-top: 4px; border-radius: 3px;
  }

  .phone {
    position: absolute; left: 238px; top: 286px;
    font-family: "Archivo Black", Arial, sans-serif; font-size: 35px; color: var(--yellow); letter-spacing: 1px;
  }
  .call-to-action {
    position: absolute; left: 16px; top: 318px;
    font-weight: 700; font-style: italic; font-size: 27px; color: var(--white);
  }
  .rule-lines { position: absolute; left: 0; top: 337px; width: 555px; height: 8px; }
  .footnote {
    position: absolute; left: 10px; top: 350px; width: 540px;
    font-size: 10.5px; font-style: italic; color: var(--white); white-space: nowrap;
  }

  .siding-photo {
    position: absolute; left: 10px; top: 45px; width: 535px; height: 200px;
    background: repeating-linear-gradient(180deg, var(--siding-a) 0 30px, var(--siding-b) 30px 34px, #1a1a1a 34px 40px);
  }
  .benefits-panel {
    position: absolute; left: 0; top: 205px; width: 555px; height: 128px; background: var(--green);
    color: var(--white); font-weight: 700; font-size: 13.5px; line-height: 1.35; text-align: center;
    padding-top: 10px;
  }
</style>
</head>
<body>

<section class="postcard postcard--front">
  <svg class="header-band" viewBox="0 0 555 45" aria-hidden="true">
    <rect width="555" height="45" fill="var(--blue)"/>
    <polygon points="300,0 555,0 555,45 270,45" fill="var(--green)"/>
  </svg>
  <h1 class="brand-title">Brightfold Exterior House Washing</h1>

  <p class="intro-box">We Clean All Types Roofs And All Types Houses And All Types Of Decks And All Types Of Surfaces With A Low Pressure Soft Wash System. We Also Try To Educate Customers About The Options And Offer A Maintenance Program So Their Property Is Never Dirty Again.</p>

  <div class="photo-row">
    <div class="photo" role="img" aria-label="Before and after photo of a cleaned roof"></div>
    <div class="photo" role="img" aria-label="Before photo of house siding"></div>
    <div class="photo" role="img" aria-label="After photo of clean house siding"></div>
  </div>

  <div class="service-badge service-badge--roof" role="img" aria-label="Soft wash roof cleaning badge"></div>
  <div class="service-badge service-badge--house" role="img" aria-label="Soft wash house washing badge"></div>
  <div class="quality-seal" role="img" aria-label="Satisfaction guarantee seal"></div>

  <div class="promise-band"><span class="lead">We Use</span><span class="figure">100%</span></div>
  <p class="promise-note">Biodegradable Solutions<br>To Achieve Results!</p>

  <p class="phone">207-555-0148</p>
  <p class="call-to-action">Call Today</p>
  <svg class="rule-lines" viewBox="0 0 555 8" aria-hidden="true">
    <line x1="0" y1="6" x2="555" y2="6" stroke="var(--green)" stroke-width="3"/>
    <line x1="330" y1="2" x2="555" y2="2" stroke="var(--blue)" stroke-width="3"/>
  </svg>
  <p class="footnote">residential and commercial work and all hoa's(home owners asoc) also group rates availiable</p>
</section>

<section class="postcard postcard--back">
  <svg class="header-band" viewBox="0 0 555 45" aria-hidden="true">
    <rect width="555" height="45" fill="var(--blue)"/>
    <polygon points="0,0 230,0 205,45 0,45" fill="var(--green)"/>
  </svg>
  <div class="siding-photo" role="img" aria-label="Close-up photo of clean horizontal house siding"></div>
  <p class="benefits-panel">Our Method Outperforms Traditional Washing<br>Methods And Remains Clean 5 Times Longer, Our Method Is 100%<br>Damage Free, Never Pressure Wash Again!!<br>Our Method Is Recommended By All Manufactures,<br>The No Pressure Method,<br>This Method Cleans So Good You Won't Believe Your Eyes! Guaranteed</p>
  <svg class="rule-lines" viewBox="0 0 555 8" aria-hidden="true">
    <line x1="0" y1="2" x2="280" y2="2" stroke="var(--blue)" stroke-width="3"/>
    <line x1="280" y1="6" x2="555" y2="6" stroke="var(--green)" stroke-width="3"/>
  </svg>
</section>

</body>
</html>
```